I need a book cover for a professional training book. I specialize in teaching financial professionals and insurance agents how to prospect and schedule first appointments by phone. My professional nickname is The DialMentor. I have been doing this training for over 30 years and am known to the industry. This book addresses the challenges the smartphone has created for the financial industry, which is a high trust profession. People are digitalizing every interaction but cannot do that with their financial advisor, so prospecting new clients has to adapt to the new world. I also address the changes the pandemic has added to this very old industry.
Please include my legal name : Merle T. Ashworth, and my nickname, The DialMentor (no spaces) on the cover
Updates

Title of my book is Booking Meetings in the Pocket Device Era. It is about how to prospect and set appointments by phone. My full name is Merle T. Ashworth and I want my branded (nickname) The DialMentor underneath it on the cover. If you want to use my logo, you can lift it from my website: www.dialmentor-example.com. My book is a training book for financial advisors, mostly newer ones. I have a built in market for a few reasons: 1. I have been training financial professionals for 30+ years. 2. I am well known in the industry. 3. Clients who hire me will buy 20 or more books at a time for their rookies. 4. I am promoting myself on WorkNexus and several professional friends tell others to buy my book. The book will not be on bookshelves in airports. It is not a novel. The industry I work in is more serious than silly. I already have a published book Current Calendar Building, Lead Finding and Calling for Money Managers. You can see it on Bookvale. I'd like to use a SIMILAR font on this book (or the same one). I do not want a purple book cover since it will create confusion between the two books. My audience runs from 22 year-olds fresh out of college to people over 60. It is not for one generation but all. I teach men, women, and all ethnicities, so I am concerned about a photo of someone holding a smartphone with obviously male/female hands. A good image will tell the story of getting appointments by phone without knowing the title. I will respond to your designs and messages quickly as I hope to make a decision soon. The book is already written and my editor is awaiting the artwork from you. Thank you in advance for accepting my project. Merle

Target Market(s)

Financial Advisors and Insurance Agents, Trainers and Manager in the financial services industry

Industry/Entity Type

Financial services, insurance

Requirements
Must have
• Clarity in the design
Should not have
• Illistrations or anything childish. This is a serious business but I don't want the cover to be boring and dour.

```html
<!DOCTYPE html>
<html lang="en">
<head>
<meta charset="UTF-8">
<title>Booking Meetings in the Pocket Device Era — Book Cover</title>
<link rel="stylesheet" href="https://fonts.googleapis.com/css2?family=Marcellus&display=swap">
<style>
  :root {
    --backdrop: #b0dbe8;
    --cover-navy: #03071a;
    --cover-deep: #020416;
    --glow-blue: #0b3f7a;
    --accent-teal: #6fd6dc;
    --band-teal: #62cfd6;
    --stripe-teal: #3a8f98;
    --ink-dark: #07101c;
    --map-grey: #8d8fae;
    --photo-dark: #0d0e14;
    --photo-warm: #d9a88a;
  }
  * { margin: 0; padding: 0; box-sizing: border-box; }
  html, body {
    width: 1200px;
    height: 899px;
    overflow: hidden;
    background: var(--backdrop);
  }
  .stage {
    position: relative;
    width: 1200px;
    height: 899px;
  }
  .book-cover {
    position: absolute;
    left: 330px;
    top: 40px;
    width: 540px;
    height: 820px;
    overflow: hidden;
    background:
      radial-gradient(ellipse 260px 360px at 40px 430px, var(--glow-blue) 0%, rgba(11,63,122,0.35) 45%, rgba(3,7,26,0) 80%),
      linear-gradient(160deg, var(--cover-navy) 0%, var(--cover-deep) 100%);
  }
  .map-texture {
    position: absolute;
    left: 260px;
    top: 70px;
    width: 170px;
    height: 330px;
    border-radius: 60% 40% 55% 45% / 30% 40% 60% 70%;
    background: linear-gradient(180deg, rgba(141,143,174,0.5) 0%, rgba(141,143,174,0.28) 70%, rgba(141,143,174,0) 100%);
    transform: rotate(-8deg);
  }
  .cover-title {
    position: absolute;
    left: 108px;
    top: 68px;
    width: 400px;
    font-family: "Marcellus", serif;
    font-weight: 400;
    color: var(--accent-teal);
    text-transform: uppercase;
    line-height: 1;
    letter-spacing: 0.5px;
  }
  .cover-title .title-line {
    display: block;
    font-size: 44px;
    margin-bottom: 8px;
    -webkit-text-stroke: 1px var(--accent-teal);
  }
  .cover-title .title-line--large {
    font-size: 82px;
    margin-bottom: 6px;
    -webkit-text-stroke: 1.5px var(--accent-teal);
  }
  .phone-photo {
    position: absolute;
    left: 270px;
    top: 400px;
    width: 270px;
    height: 300px;
    background: linear-gradient(120deg, var(--photo-dark) 0%, var(--photo-dark) 45%, var(--photo-warm) 100%);
    opacity: 0.9;
  }
  .stripe-block {
    position: absolute;
    background: var(--stripe-teal);
  }
  .stripe-block--top {
    left: 40px;
    top: 664px;
    width: 90px;
    height: 22px;
    border-radius: 40px 40px 0 0;
  }
  .stripe-block--bottom {
    left: 40px;
    top: 760px;
    width: 150px;
    height: 60px;
  }
  .author-band {
    position: absolute;
    left: 40px;
    top: 685px;
    width: 500px;
    height: 76px;
    background: var(--band-teal);
    text-align: center;
    padding-top: 11px;
  }
  .author-name {
    font-family: "Marcellus", serif;
    font-size: 36px;
    color: var(--ink-dark);
    letter-spacing: 0.5px;
    line-height: 1;
    -webkit-text-stroke: 1px var(--ink-dark);
  }
  .author-nickname {
    display: flex;
    align-items: center;
    justify-content: center;
    gap: 8px;
    margin-top: 5px;
    font-family: "Marcellus", serif;
    font-size: 15px;
    line-height: 1;
    color: var(--ink-dark);
    letter-spacing: 1px;
  }
  .author-nickname .rule {
    width: 100px;
    height: 1.5px;
    background: var(--ink-dark);
  }
</style>
</head>
<body>
  <main class="stage">
    <section class="book-cover" aria-label="Book cover: Booking Meetings in the Pocket Device Era by Merle T. Ashworth">
      <div class="map-texture" role="img" aria-label="Faint dotted world map texture behind the title"></div>

      <h1 class="cover-title">
        <span class="title-line title-line--large">Booking</span>
        <span class="title-line">Meetings</span>
        <span class="title-line">In the</span>
        <span class="title-line">Pocket Device</span>
        <span class="title-line title-line--large">Era</span>
      </h1>

      <div class="phone-photo" role="img" aria-label="Photo of a hand holding a smartphone showing an appointment confirmation icon"></div>

      <div class="stripe-block stripe-block--top" aria-hidden="true"></div>
      <div class="stripe-block stripe-block--bottom" aria-hidden="true"></div>

      <div class="author-band">
        <p class="author-name">MERLE T. ASHWORTH</p>
        <p class="author-nickname"><span class="rule"></span>(DIALMENTOR)<span class="rule"></span></p>
      </div>
    </section>
  </main>
</body>
</html>
```